Professional window cleaning services business needs a flyer design

We are looking to attract large businesses such as gyms, car dealerships and fast food restaurants.
-Have over 15 years of experience in this business
-We serve customers in Melbourne and all surrounding suburbs
-Specialising in automated periodical services(daily,weekly,monthly, yearly)
-Our current client base consists of major fast food restaurants, car dealerships and residential properties.

Industry/Entity Type

Window Cleaning

Colors
3176b5
fbed22

Requirements
Must have
• Business Details:
• Name: Brightpane Window Cleaning
• Phone no:95402367
• website:www.quorlinpro.com.au
• email: admin@quorlinpro.com.au
• mail: PO BOX 4826, Marrowdale Heights, 3478

```html
<!DOCTYPE html>
<html lang="en">
<head>
<meta charset="utf-8">
<title>Brightpane Window Cleaning – Flyer</title>
<link href="https://fonts.googleapis.com/css2?family=Open+Sans:wght@300;400;600;700;800&display=swap" rel="stylesheet">
<style>
  :root {
    --brand-blue: #3176b5;
    --deep-blue: #2b64a0;
    --brand-yellow: #fbed22;
    --burst-text: #1f4f86;
    --accent-orange: #ee7d1e;
    --white: #ffffff;
    --photo-sky: #b9c6d2;
    --photo-ground: #7d8a6a;
  }
  * { margin: 0; padding: 0; box-sizing: border-box; }
  html, body { width: 852px; height: 1200px; overflow: hidden; background: var(--white); }
  body { font-family: "Open Sans", Arial, sans-serif; }
  .flyer { position: relative; width: 852px; height: 1200px; overflow: hidden; background: var(--white); }

  .header-brand {
    position: absolute; left: 34px; top: 22px;
    font-size: 40px; font-weight: 800; color: var(--brand-yellow);
    letter-spacing: 1px; line-height: 1;
  }
  .header-title {
    position: absolute; right: 36px; top: 38px;
    font-size: 22px; font-weight: 800; color: var(--brand-blue);
    letter-spacing: -0.3px;
  }

  .hero-photo {
    position: absolute; left: 0; top: 92px; width: 852px; height: 490px;
    background: linear-gradient(180deg, var(--photo-sky) 0%, #d5dde4 45%, var(--photo-ground) 62%, #6d6f6a 100%);
  }

  .shapes { position: absolute; left: 0; top: 0; }

  .services {
    position: absolute; left: 274px; top: 596px; width: 300px; text-align: center;
  }
  .services-heading { font-size: 21px; font-weight: 700; color: var(--white); letter-spacing: -0.5px; margin-bottom: 6px; }
  .services-list { list-style: none; }
  .services-list li { font-size: 17px; font-weight: 300; color: var(--brand-yellow); line-height: 29px; letter-spacing: -0.6px; }

  .free-quote {
    position: absolute; left: 40px; top: 690px; width: 260px; text-align: center;
    transform: rotate(-11deg); color: var(--white); font-weight: 700; line-height: 1.15;
  }
  .free-quote .quote-big { font-size: 24px; }
  .free-quote .quote-line { font-size: 21px; }

  .experience {
    position: absolute; left: 605px; top: 700px; width: 120px; text-align: center;
    font-size: 15px; font-weight: 700; color: var(--burst-text); line-height: 23px; letter-spacing: -0.4px;
  }

  .schedule-note {
    position: absolute; left: 0; top: 898px; width: 852px; padding-left: 0; text-align: center;
    font-size: 12.5px; color: var(--white);
  }
  .schedule-note span { position: relative; left: 0; }

  .divider-brand {
    position: absolute; left: 360px; top: 924px; width: 132px; text-align: center;
    font-size: 22px; font-weight: 800; color: var(--brand-yellow); line-height: 32px;
    background: var(--brand-blue);
  }

  .call-block { position: absolute; left: 40px; top: 1012px; width: 390px; text-align: center; }
  .call-heading { font-size: 44px; font-weight: 300; color: var(--brand-yellow); line-height: 1; }
  .call-number { font-size: 62px; font-weight: 400; color: var(--white); line-height: 1.2; letter-spacing: -1px; }
  .call-area { font-size: 12.5px; color: var(--white); margin-top: 2px; }

  .contact-details {
    position: absolute; left: 450px; top: 1042px; width: 340px; text-align: center;
    list-style: none; color: var(--white); font-size: 16.5px; font-weight: 400; line-height: 39px;
    text-transform: uppercase; letter-spacing: -0.2px;
  }
</style>
</head>
<body>
<main class="flyer">
  <div class="header-brand">BRIGHTPANE</div>
  <h1 class="header-title">BRIGHTPANE WINDOW CLEANING</h1>

  <div class="hero-photo" role="img" aria-label="Photograph of a window cleaner standing beside a yellow branded service van with ladders on its roof rack, parked at a roadside"></div>

  <svg class="shapes" width="852" height="1200" viewBox="0 0 852 1200" aria-hidden="true">
    <path d="M0 534 Q300 600 852 500 L852 942 L0 942 Z" fill="var(--brand-blue)"/>
    <rect x="0" y="940" width="852" height="6" fill="var(--white)"/>
    <rect x="0" y="946" width="852" height="254" fill="var(--brand-blue)"/>
    <polygon fill="var(--brand-yellow)" points="665,635 682,693 730,656 710,713 770,711 720,745 770,779 710,777 730,834 682,797 665,855 648,797 600,834 620,777 560,779 610,745 560,711 620,713 600,656 648,693"/>
    <path d="M472 972 L786 990 Q808 992 808 1016 L808 1210 L444 1210 L444 1000 Q444 970 472 972 Z" fill="var(--accent-orange)" stroke="var(--white)" stroke-width="5"/>
  </svg>

  <section class="services">
    <h2 class="services-heading">SERVICES</h2>
    <ul class="services-list">
      <li>HIGH RISE SERVICES</li>
      <li>RESIDENTIAL SERVICES</li>
      <li>CORPORATE SERVICES</li>
      <li>COMMERCIAL SERVICES</li>
      <li>GUTTER SERVICES</li>
      <li>ROOF SERVICES</li>
      <li>PRESSURE SERVICES</li>
      <li>BLIND SERVICES</li>
      <li>CONSULTING SERVICES</li>
    </ul>
  </section>

  <div class="free-quote">
    <div class="quote-big">FREE</div>
    <div class="quote-line">WINDOW CLEANING</div>
    <div class="quote-line">QUOTE</div>
  </div>

  <div class="experience">OVER<br>15 YEARS OF<br>EXPERIENCE</div>

  <p class="schedule-note"><span>Specialising in automated periodical services ( daily,weekly,monthly, yearly )</span></p>

  <div class="divider-brand">BRIGHTPANE</div>

  <section class="call-block">
    <div class="call-heading">CALL US TODAY</div>
    <div class="call-number">9540 2367</div>
    <p class="call-area">We serve customers in Melbourne and all surrounding suburbs</p>
  </section>

  <ul class="contact-details">
    <li>www.quorlinpro.com.au</li>
    <li>admin@quorlinpro.com.au</li>
    <li>PO BOX 4826, Marrowdale Heights, 3478</li>
  </ul>
</main>
</body>
</html>
```